Tolsán & Quiroga, Vendrexa exclusive agency

I need you to make me designs for my company's business cards, we are an Vendrexa Exclusive Agency.

Target Market(s)

Business

Contact Information for Business Card

Debe contener:
- El logo de la Agencia.
- El logo de Vendrexa
- El nombre de la empresa Tolsán & Quiroga
- La pag web www.tolsanquiroga-ejemplo.com y el código QR de la web
- El Facebook corporativo: facebook.com/vendrexa.seguros.tolsanquirogasl
- tlf: 900 47 52 36
- Móvil: 612 90 24 77
Mi nombre: Tomás Lorente Quiroga

Oficinas: Cl. Almendro, núm. 482, 3°, Oficina 14, 32005, Ourense
Cl. Fermín Otero, núm. 9, 4° Oficinas A-B, 36214, Vigo.

El correo electrónico: info@tolsanquiroga-ejemplo.com

Font styles to use
Sans Serif

Requirements
Must have
• You must maintain corporate colors. Can be on blue background or on white background. Part ahead: - The Agency logo should go in the upper left. - The Vendrexa logo should be smaller in the upper right - p. Web and Facebook. - Personal data, name, telephones and mail Back: - QR code of the web. - Offices and location of the same It will be valued that they play with the corporate colors in letters and design, besides introducing watermarks of the logo in the back part.
Nice to have
• The letter in Tahoma or Arial

```html
<!DOCTYPE html>
<html lang="es">
<head>
<meta charset="utf-8">
<title>Tolsán &amp; Quiroga — Tarjetas de visita</title>
<link rel="stylesheet" href="https://fonts.googleapis.com/css2?family=Archivo+Black&family=Arimo:wght@400;700&family=Montserrat:wght@600&display=swap">
<style>
  :root {
    --navy: #1d3a78;
    --brand-blue: #23477f;
    --brand-green: #78b83a;
    --paper: #efeeec;
    --stage: #22345f;
    --card-blue-light: #2b5f98;
    --card-blue-dark: #132f66;
    --white: #ffffff;
  }
  * { box-sizing: border-box; margin: 0; padding: 0; }
  html, body { width: 1200px; height: 900px; overflow: hidden; }
  body { background: var(--stage); position: relative; font-family: "Arimo", Arial, sans-serif; }

  .card { position: absolute; overflow: hidden; }

  /* Front: portrait white card */
  .card-front {
    left: 134px; top: 170px; width: 336px; height: 588px;
    background: var(--paper);
  }
  .holder-name {
    position: absolute; left: 37px; top: 38px;
    font-family: "Archivo Black", Arial, sans-serif;
    font-size: 17px; letter-spacing: 0.3px; color: var(--brand-blue);
    white-space: nowrap;
  }
  .holder-role {
    position: absolute; left: 37px; top: 62px;
    font-size: 13px; letter-spacing: 1px; color: var(--brand-green);
  }
  .role-rule {
    position: absolute; left: 37px; top: 86px; width: 20px; height: 2px;
    background: var(--brand-green);
  }
  .agency-mark {
    position: absolute; left: 0; right: 0; top: 212px;
    text-align: center;
  }
  .mark-square {
    display: inline-block; width: 58px; height: 58px;
    background: var(--brand-blue);
  }
  .agency-name {
    font-family: "Montserrat", Arial, sans-serif; font-weight: 600;
    font-size: 23px; color: var(--brand-green); margin-top: 16px;
    white-space: nowrap;
  }
  .agency-tagline {
    font-size: 11px; font-weight: 700; color: var(--brand-blue);
    margin-top: 4px;
  }
  .contact-list {
    position: absolute; right: 33px; top: 488px;
    text-align: right; list-style: none;
    font-size: 14px; color: var(--brand-blue); line-height: 24px;
  }
  .contact-list .accent { color: var(--brand-green); }
  .social-square {
    display: inline-block; width: 12px; height: 12px;
    background: var(--brand-blue); margin-left: 5px; vertical-align: -1px;
  }
  .edge-tab {
    position: absolute; right: 0; top: 494px; width: 22px; height: 56px;
    background: var(--brand-blue);
  }

  /* Back: landscape blue card */
  .card-back {
    left: 518px; top: 464px; width: 549px; height: 294px;
    background: radial-gradient(circle at 15% 10%, var(--card-blue-light), var(--card-blue-dark) 85%);
  }
  .back-lockup {
    position: absolute; left: 126px; top: 110px;
    display: flex; align-items: center; gap: 14px;
  }
  .back-square { width: 56px; height: 56px; background: var(--white); }
  .back-name {
    font-family: "Montserrat", Arial, sans-serif; font-weight: 600;
    font-size: 25px; color: var(--brand-green); line-height: 1; white-space: nowrap;
  }
  .back-tagline {
    font-size: 12px; font-weight: 700; color: var(--white);
    letter-spacing: 2.2px; margin-top: 6px; white-space: nowrap;
  }
</style>
</head>
<body>

<section class="card card-front">
  <h1 class="holder-name">TOMÁS LORENTE QUIROGA</h1>
  <p class="holder-role">MANAGING DIRECTOR</p>
  <div class="role-rule"></div>

  <div class="agency-mark">
    <span class="mark-square"></span>
    <p class="agency-name">Tolsán &amp; Quiroga</p>
    <p class="agency-tagline">Agencia exclusiva Vendrexa</p>
  </div>

  <ul class="contact-list">
    <li>info@tolsanquiroga-ejemplo.com</li>
    <li>www.<span class="accent">tolsanquiroga-ejemplo</span>.com</li>
    <li>tolsanquiroga-ejemplo<span class="social-square"></span></li>
  </ul>
  <div class="edge-tab"></div>
</section>

<section class="card card-back">
  <div class="back-lockup">
    <div class="back-square"></div>
    <div>
      <p class="back-name">Tolsán &amp; Quiroga</p>
      <p class="back-tagline">Agencia exclusiva Vendrexa</p>
    </div>
  </div>
</section>

</body>
</html>
```